Menu revision for Korean Restaurant

I have posted the exact content in a word file that I would like to appear in the menu. Please apply to the template. I will be following up with prices shortly. I am in a hurry and not too picky. Thank you.

Make a menu with revisions.

Page 1: Cover Page
- Replace logo with new uploaded logo

Page 2:
Appetizers
Vegetarian Appetizers

Page 3:
BBQ Items

Page 4:
Signature Dishes

Page 5:
Bokkeum | Stir-Fry

Page 6:
Rice Bowls
Noodles
Hot Soup

Page 7:
Drinks

Target Market(s)

My customers

Industry/Entity Type

Restaurant

Requirements
Must have
• 1. Only use my menu content, template, and font.

```html
<!DOCTYPE html>
<html lang="en">
<head>
<meta charset="utf-8">
<title>Appetizers Menu</title>
<link rel="stylesheet" href="https://fonts.googleapis.com/css2?family=Barlow+Condensed:wght@700&family=Barlow+Semi+Condensed:wght@600&family=Lora:wght@400&family=Nanum+Gothic:wght@400;700&display=swap">
<style>
  :root {
    --bg: #333333;
    --gold: #b6a173;
    --gold-line: #9c8a60;
    --red: #c0393d;
    --ink: #f2f0ea;
  }
  * { margin: 0; padding: 0; box-sizing: border-box; }
  html, body { width: 928px; height: 1200px; overflow: hidden; background: var(--bg); }
  .menu-page { position: relative; width: 928px; height: 1200px; background: var(--bg); }
  .frame { position: absolute; inset: 0; }
  .section-title {
    position: absolute; left: 0; width: 100%; text-align: center;
    font-family: "Barlow Condensed", "Oswald", sans-serif; font-weight: 700;
    color: var(--red); font-size: 68px; letter-spacing: 1px; line-height: 1;
  }
  .item {
    position: absolute; font-family: "Barlow Semi Condensed", "Barlow", sans-serif;
    font-weight: 600; font-size: 14px; color: var(--gold); line-height: 18px;
  }
  .item .ko { font-family: "Nanum Gothic", sans-serif; font-weight: 400; font-size: 13px; margin-left: 4px; }
  .item .desc {
    font-family: "Lora", "Georgia", serif; font-weight: 400; color: var(--ink);
    font-size: 14.5px; margin-left: 2px;
  }
  .item.wide { width: 388px; text-align: justify; line-height: 18.5px; }
  .note {
    position: absolute; font-family: "Lora", "Georgia", serif; color: var(--ink);
    font-size: 14px; line-height: 18px;
  }
  .divider { position: absolute; left: 0; width: 928px; height: 60px; }
</style>
</head>
<body>
<main class="menu-page">
  <svg class="frame" width="928" height="1200" viewBox="0 0 928 1200" aria-hidden="true">
    <g fill="none" stroke="var(--gold-line)" stroke-width="1.5">
      <path d="M66 31 H862 M66 1169 H862 M31 66 V1134 M897 66 V1134"/>
      <path d="M66 31 V66 H31"/>
      <path d="M862 31 V66 H897"/>
      <path d="M66 1169 V1134 H31"/>
      <path d="M862 1169 V1134 H897"/>
      <rect x="46" y="46" width="20" height="20"/>
      <rect x="862" y="46" width="20" height="20"/>
      <rect x="46" y="1134" width="20" height="20"/>
      <rect x="862" y="1134" width="20" height="20"/>
    </g>
  </svg>

  <h1 class="section-title" style="top:48px;">APPETIZERS</h1>

  <div class="item" style="left:59px; top:130px;">Mandu<span class="ko">군만두</span></div>
  <div class="item" style="left:59px; top:164px;">Mul Mandu<span class="ko">물만두</span></div>
  <div class="item" style="left:61px; top:198px;">Chicken Wings<span class="ko">닭날개</span></div>
  <div class="item" style="left:61px; top:232px;">Spicy Wings<span class="ko">닭날개</span></div>
  <div class="item" style="left:59px; top:268px;">Yang Yum Chicken<span class="ko">양념치킨</span></div>

  <div class="item" style="left:478px; top:130px;">Shrimp Tempura<span class="ko">새우튀김</span></div>
  <div class="item" style="left:478px; top:164px;">Fried Calamari<span class="ko">오징어튀김</span></div>
  <div class="item wide" style="left:478px; top:198px;">Haemul Pajeon<span class="ko">해물파전</span><span class="desc">Assortment of fresh calamari, shrimp, scallops, mussels, and scallions in a Korean pancake.</span></div>
  <p class="note" style="left:478px; top:272px;">*Jeon batter contains wheat flour &amp; eggs.</p>

  <svg class="divider" style="top:312px;" viewBox="0 0 928 60" aria-hidden="false">
    <path d="M255 30 H414 M490 30 H642" stroke="var(--gold-line)" stroke-width="1.5"/>
    <circle cx="452" cy="30" r="23" fill="var(--gold-line)" role="img" aria-label="Round gold emblem ornament"/>
  </svg>

  <h2 class="section-title" style="top:445px;">VEGETARIAN APPETIZERS</h2>

  <div class="item" style="left:59px; top:545px;">Veggie Mandu<span class="ko">야채만두</span></div>
  <div class="item" style="left:59px; top:580px;">Veggie Mul Mandu<span class="ko">야채물만두</span></div>
  <div class="item" style="left:59px; top:616px;">Sweet Potato Tempura<span class="ko">고구마튀김</span></div>
  <div class="item" style="left:59px; top:650px;">Veggie Tempura<span class="ko">야채튀김</span></div>
  <div class="item" style="left:59px; top:687px;">Mushroom Tempura<span class="ko">버섯튀김</span></div>

  <div class="item" style="left:478px; top:545px;">Pajeon<span class="ko">파전</span><span class="desc">Pan fried green onion pancake</span></div>
  <div class="item wide" style="left:478px; top:580px;">Hobak Gochu Jeon<span class="ko">호박고추전</span><span class="desc">Zucchini and Jalapeño pancake</span></div>
  <div class="item wide" style="left:478px; top:641px;">Kimchi Pajeon<span class="ko">김치파전</span><span class="desc">Crispy kimchi and scallion pancake</span></div>
  <p class="note" style="left:478px; top:701px;">*Jeon batter contains wheat flour &amp; eggs.</p>

  <svg class="divider" style="top:743px;" viewBox="0 0 928 60" aria-hidden="false">
    <path d="M255 30 H414 M490 30 H642" stroke="var(--gold-line)" stroke-width="1.5"/>
    <circle cx="452" cy="30" r="23" fill="var(--gold-line)" role="img" aria-label="Round gold emblem ornament"/>
  </svg>
</main>
</body>
</html>
```